Home Staging Company needs business card design

We're a home staging company called Brightwell Harbor Home Staging. We would like a business card design that includes aqua and gray. Our current logo of house within chair is fine but I find we almost always use the logo in one color. I'll upload images of front and back of our current card and our logo. Note that we have dropped "Solutions" from our company name and don't want to include it on the card.

Target Market(s)

Realtors and homeowners - people interested in selling their homes

Contact Information for Business Card

Marisol Fenwickley
Brightwell Harbor Home Staging
757-382-6190
www.brightwellharbor.com
marisol@brightwellharbor.com

Font styles to use
Serif
Script

Requirements
Must have
• My logo and contact details
• UPDATE***
• I forgot to say that the company name should be included on the front of the card somehow.

```html
<!DOCTYPE html>
<html lang="en">
<head>
<meta charset="utf-8">
<title>Brightwell Harbor Home Staging – Business Card</title>
<link rel="stylesheet" href="https://fonts.googleapis.com/css2?family=Cormorant+Garamond:wght@500;600&family=Montserrat:wght@400&display=swap">
<style>
  :root {
    --backdrop: #3a3a3c;
    --aqua: #2ba4ae;
    --charcoal: #2a2a2b;
    --white: #ffffff;
    --soft-white: #e9e9e9;
    --serif: "Cormorant Garamond", Georgia, serif;
    --sans: "Montserrat", Arial, sans-serif;
  }
  * { box-sizing: border-box; margin: 0; padding: 0; }
  html, body { width: 1200px; height: 752px; overflow: hidden; }
  body {
    background: var(--backdrop);
    position: relative;
  }
  .card {
    position: absolute;
    top: 226px;
    width: 500px;
    height: 300px;
    box-shadow: 0 18px 40px rgba(0,0,0,0.35);
  }
  .card--front { left: 70px; background: var(--aqua); }
  .card--back { left: 630px; background: var(--charcoal); }

  .brand {
    display: flex;
    align-items: center;
    gap: 12px;
    position: absolute;
    left: 0; right: 0;
    justify-content: center;
  }
  .brand__mark {
    width: 34px; height: 34px;
    border-radius: 50%;
    flex: none;
  }
  .brand__name {
    font-family: var(--serif);
    font-weight: 600;
    color: var(--white);
    white-space: nowrap;
  }

  .card--front .brand { top: 112px; }
  .card--front .brand__mark { background: var(--white); }
  .card--front .brand__name { font-size: 25px; }
  .card--front .website {
    position: absolute;
    left: 0; right: 0; top: 218px;
    text-align: center;
    font-family: var(--sans);
    font-size: 11px;
    letter-spacing: 0.06em;
    color: var(--white);
  }

  .card--back .brand { top: 62px; gap: 10px; }
  .card--back .brand__mark { width: 26px; height: 26px; background: var(--aqua); }
  .card--back .brand__name { font-size: 18px; }

  .person {
    position: absolute;
    left: 0; right: 0; top: 130px;
    text-align: center;
    font-family: var(--serif);
    font-weight: 500;
    font-variant: small-caps;
    font-size: 21px;
    letter-spacing: 0.06em;
    color: var(--white);
  }
  .contact {
    position: absolute;
    left: 0; right: 0; top: 170px;
    list-style: none;
    text-align: center;
    font-family: var(--sans);
    font-size: 10.5px;
    line-height: 15px;
    letter-spacing: 0.04em;
    color: var(--soft-white);
  }
  .social {
    position: absolute;
    left: 0; right: 0; top: 232px;
    display: flex;
    justify-content: center;
    gap: 8px;
  }
  .social__dot {
    width: 9px; height: 9px;
    border-radius: 50%;
    background: var(--soft-white);
  }
</style>
</head>
<body>
  <section class="card card--front" aria-label="Card front">
    <div class="brand">
      <span class="brand__mark"></span>
      <span class="brand__name">Brightwell Harbor Home Staging</span>
    </div>
    <p class="website">www.brightwellharbor.com</p>
  </section>

  <section class="card card--back" aria-label="Card back">
    <div class="brand">
      <span class="brand__mark"></span>
      <span class="brand__name">Brightwell Harbor Home Staging</span>
    </div>
    <p class="person">Marisol Fenwickley</p>
    <ul class="contact">
      <li>757-382-6190</li>
      <li>marisol@brightwellharbor.com</li>
      <li>www.brightwellharbor.com</li>
    </ul>
    <div class="social" aria-label="Social profiles">
      <span class="social__dot"></span>
      <span class="social__dot"></span>
      <span class="social__dot"></span>
    </div>
  </section>
</body>
</html>
```